Email Signature

We would like to have an email Signature designed.
We have an idea, and a logo that we would like to be make more professional in design and look.

```html
<!DOCTYPE html>
<html lang="en">
<head>
<meta charset="utf-8">
<title>Email Signature – Tenfold Advisory</title>
<link href="https://fonts.googleapis.com/css2?family=Open+Sans:wght@400;600;700&display=swap" rel="stylesheet">
<style>
  :root {
    --page-bg: #d9d9dc;
    --card-bg: #ffffff;
    --brand-blue: #1a73c7;
    --brand-orange: #f05a2a;
    --wave-light: #f1f1f2;
    --wave-dark: #c9c9cc;
    --rule: #c8c8cc;
  }
  * { margin: 0; padding: 0; box-sizing: border-box; }
  html, body {
    width: 1200px; height: 398px; overflow: hidden;
    background: var(--page-bg);
    font-family: "Open Sans", Arial, sans-serif;
  }
  .signature {
    position: absolute; left: 43px; top: 90px;
    width: 1114px; height: 233px;
    background: var(--card-bg);
    overflow: hidden;
  }
  .signature__waves { position: absolute; inset: 0; }
  .brand {
    position: absolute; left: 180px; top: 68px;
    display: flex; align-items: center; gap: 14px;
  }
  .brand__dot {
    width: 48px; height: 48px; border-radius: 50%;
    background: var(--brand-orange);
  }
  .brand__name {
    color: var(--brand-blue);
    font-weight: 700; font-size: 36px; line-height: 38px;
    letter-spacing: 0.5px;
  }
  .contact {
    position: absolute; left: 897px; top: 84px;
    color: var(--brand-blue);
  }
  .contact__name { font-size: 20px; font-weight: 700; line-height: 26px; }
  .contact__role {
    font-size: 15px; line-height: 22px;
    padding-bottom: 6px; margin-bottom: 8px;
    border-bottom: 1px solid var(--rule);
    width: 180px;
  }
  .contact__line {
    display: flex; align-items: center; gap: 8px;
    font-size: 16px; line-height: 25px;
  }
  .contact__icon { width: 15px; height: 15px; flex: none; }
</style>
</head>
<body>
  <section class="signature">
    <svg class="signature__waves" width="1114" height="233" viewBox="0 0 1114 233" aria-hidden="true">
      <defs>
        <linearGradient id="waveFill" x1="0" y1="0" x2="1" y2="0">
          <stop offset="0" stop-color="var(--wave-light)"/>
          <stop offset="0.55" stop-color="#e6e6e8"/>
          <stop offset="1" stop-color="var(--wave-dark)"/>
        </linearGradient>
      </defs>
      <path d="M0,178 C100,205 220,216 320,215 C520,212 620,60 800,38 C900,27 1000,22 1114,24 L1114,233 L0,233 Z" fill="url(#waveFill)"/>
      <path d="M800,38 C900,27 1000,22 1114,24" fill="none" stroke="#bdbdc1" stroke-width="1"/>
      <path d="M0,135 C40,175 130,207 250,214 C140,214 60,200 0,188 Z" fill="var(--brand-orange)"/>
      <path d="M0,100 C40,155 150,208 300,215 L320,215 C180,216 70,190 0,150 Z" fill="var(--brand-blue)"/>
    </svg>

    <div class="brand">
      <span class="brand__dot"></span>
      <span class="brand__name">Tenfold<br>Advisory</span>
    </div>

    <div class="contact">
      <p class="contact__name">Sam Whitford</p>
      <p class="contact__role">Client Relations</p>
      <p class="contact__line">
        <svg class="contact__icon" viewBox="0 0 16 16" aria-hidden="true">
          <circle cx="8" cy="8" r="8" fill="var(--brand-orange)"/>
          <path d="M5.2,4.2 L6.6,4 L7.3,5.9 L6.4,6.6 C6.9,7.7 7.9,8.7 9,9.2 L9.7,8.3 L11.6,9 L11.4,10.4 C8,10.8 4.8,7.6 5.2,4.2 Z" fill="#fff"/>
        </svg>
        +61 400 123 987
      </p>
      <p class="contact__line">
        <svg class="contact__icon" viewBox="0 0 16 16" aria-hidden="true">
          <circle cx="8" cy="8" r="8" fill="var(--brand-orange)"/>
          <circle cx="8" cy="8" r="4" fill="none" stroke="#fff" stroke-width="1.2"/>
          <path d="M4,8 H12 M8,4 C6.5,6 6.5,10 8,12 M8,4 C9.5,6 9.5,10 8,12" fill="none" stroke="#fff" stroke-width="1"/>
        </svg>
        www.tfadvisory.com.au
      </p>
    </div>
  </section>
</body>
</html>
```